R.T. Wexmoor Electrical work flyer

I need a flyer design to help generate some extra work. I'm more than happy for a designer to play around with pictures, text, headings, boarders. The flyer will be double sided A4 size.
We specialize in Residential, Commercial, & Industrial Electrical works including PV Solar System Designs & Installations, Maintenance, System Checks & Upgrades, Mains Upgrades, Overhead & Underground, Switchboard Installations & Upgrades, Safety Switches, Spa & Pool connections, LED Lighting solutions, Energy Audit Checks, Fans & Air Conditioning, Hi-bay Lighting, Carpark Lighting, Data Points, Comms Racks, New Home Builds, Office Fitouts ...
We pride ourselves on always doing a great job, guaranteed workmanship, competitive pricing, & leaving the site clean.
Call Derek for a quote on any of your electrical needs
Mobile:0418 736 204
Email: rtwexmoorelectrical@quillmail.test
PO Box 58
Brambleton Vale VIC 3179

LEN: 38517
NRB Accreditation: A3182609

I've added my company logo & some pics, photo's & electrical / solar brand logos that can be used but not a must. I'm more than happy if you can find better pics.

Target Market(s)

Office, Factory & Home Owners

Industry/Entity Type

Electrical

Font styles to use
Serif
Sans Serif

Requirements
Must have
• eye catchy design with not to much information overload.
• Just aiming for people to call up for quotes etc.
Nice to have
• My company logo, electrical & solar works available
Should not have
• pictures of kids

```html
<!DOCTYPE html>
<html lang="en">
<head>
<meta charset="utf-8">
<title>R.T. Wexmoor Electrical – Flyer</title>
<link rel="stylesheet" href="https://fonts.googleapis.com/css2?family=Open+Sans:wght@400;600&family=Roboto+Condensed:wght@300;400&family=Oswald:wght@400;500&display=swap">
<style>
:root{
  --green:#6aa84f;
  --green-dark:#4f8f35;
  --green-light:#8cc063;
  --charcoal:#3c3d3f;
  --ink:#222;
  --grey-text:#4a4a4a;
  --header-bg:#efefef;
  --page:#ffffff;
  --backdrop:#e4e2df;
}
*{box-sizing:border-box;margin:0;padding:0}
html,body{width:1200px;height:905px;overflow:hidden}
body{background:var(--backdrop);font-family:"Open Sans",sans-serif;color:var(--ink);position:relative}
.flyer{position:absolute;top:70px;width:540px;height:765px;background:var(--page);overflow:hidden;box-shadow:0 6px 18px rgba(0,0,0,.18)}
.flyer--front{left:40px}
.flyer--back{left:620px}

/* brand lockup */
.brand{display:flex;align-items:center;gap:12px}
.brand__dot{width:50px;height:50px;border-radius:50%;background:var(--green);flex:none}
.brand__name{font-family:"Open Sans",sans-serif;font-weight:600;color:var(--grey-text);line-height:1.05;font-size:28px;letter-spacing:.5px}

/* front */
.front__topline{position:absolute;top:0;left:0;right:0;height:12px;background:var(--green)}
.front__header{position:absolute;top:12px;left:0;right:0;height:101px;background:linear-gradient(#f6f6f6,#e9e9e9);padding:22px 0 0 24px}
.front__creds{position:absolute;right:22px;top:48px;text-align:right;font-family:"Roboto Condensed",sans-serif;font-size:13px;line-height:21px;color:#444}
.front__photo{position:absolute;top:113px;left:0;right:0;height:290px;background:linear-gradient(180deg,#c9d2da 0%,#eef2f5 40%,#d5dde3 70%,#aab6c0 100%)}
.band{position:absolute;left:0;color:#fff;font-family:"Roboto Condensed",sans-serif;font-weight:400;white-space:nowrap;padding-left:14px}
.band--dark{background:var(--charcoal)}
.band--green{background:var(--green)}
.front__band{top:383px;width:448px;height:38px;line-height:38px;font-size:14.5px;clip-path:polygon(0 0,420px 0,448px 100%,0 100%)}
.tagline{position:absolute;top:438px;left:0;right:0;text-align:center;font-family:"Roboto Condensed",sans-serif;font-weight:400;font-size:16.5px;line-height:27px;letter-spacing:-.2px;color:#222}
.thumb{position:absolute;width:128px;height:128px;border-radius:50%;border:3px solid var(--green)}
.thumb::after{content:"";position:absolute;left:10px;right:10px;bottom:-22px;height:8px;border-radius:50%;background:radial-gradient(rgba(0,0,0,.28),rgba(0,0,0,0) 70%)}
.thumb--office{background:linear-gradient(#e4e8ea,#9aa39f)}
.thumb--warehouse{background:linear-gradient(#6f7a83,#d7dadd)}
.thumb--home{background:linear-gradient(#c9bcd4,#8a7f78)}
.thumb--spa{background:radial-gradient(circle at 45% 50%,#5ec8ff,#0a4f86 70%,#072a4a)}
.thumb--board{background:linear-gradient(90deg,#bfc3c2,#e9ece9 50%,#a9aeaa)}
.thumb--carpark{background:linear-gradient(#08121f 0%,#162434 60%,#3b3f44 100%)}

.footer{position:absolute;left:0;right:0;bottom:0;height:84px;background:linear-gradient(90deg,var(--green) 0%,var(--green-light) 100%);color:#fff}
.contact{position:absolute;left:16px;top:30px;font-family:"Oswald",sans-serif;font-weight:400;font-size:13px;line-height:21px;list-style:none}
.contact li{display:flex;align-items:center;gap:5px}
.contact svg{width:10px;height:10px}
.quote{position:absolute;right:18px;top:14px;display:flex;align-items:center;gap:10px}
.quote__icon{width:26px;height:58px}
.quote__label{font-family:"Oswald",sans-serif;font-size:18px;line-height:20px;letter-spacing:.3px}
.quote__number{font-family:"Oswald",sans-serif;font-weight:500;font-size:38px;line-height:40px;letter-spacing:1px}

/* back */
.back__photo{position:absolute;top:0;left:0;right:0;height:253px;background:linear-gradient(180deg,#bcd3e4 0%,#dfe7ec 28%,#3a4a66 45%,#6a7c98 70%,#c9d1d9 100%)}
.back__header{position:absolute;top:0;left:0;width:540px;height:120px}
.back__brand{position:absolute;top:28px;left:16px}
.back__band{top:235px;width:420px;height:37px;line-height:37px;font-size:14px;clip-path:polygon(0 0,398px 0,420px 100%,0 100%)}
.back__band2{top:273px;width:407px;height:28px;line-height:28px;font-size:14px}
.services{position:absolute;top:321px;list-style:none;font-family:"Open Sans",sans-serif;font-size:14.5px;line-height:17.3px;color:#111}
.services li::before{content:"» ";color:var(--green)}
.services--left{left:28px}
.services--right{left:330px}
.partners{position:absolute;top:642px;left:14px;right:14px;display:flex;justify-content:space-between;align-items:center}
.partners span{display:block;height:20px;border-radius:3px;background:#c9cbcd}
</style>
</head>
<body>

<!-- FRONT -->
<section class="flyer flyer--front">
  <div class="front__topline"></div>
  <header class="front__header">
    <div class="brand">
      <span class="brand__dot"></span>
      <div class="brand__name">R.T. Wexmoor<br>Electrical</div>
    </div>
    <div class="front__creds">LEN: 38517<br>NRB Accreditation: A3182609</div>
  </header>
  <div class="front__photo" role="img" aria-label="Bright open-plan commercial office floor with rows of ceiling lights"></div>
  <div class="band band--dark front__band">RESIDENTIAL, COMMERCIAL, &amp; INDUSTRIAL ELECTRICAL WORKS</div>
  <p class="tagline">We pride ourselves on always doing a great job, guaranteed workmanship,<br>competitive pricing, &amp; leaving the site clean.</p>
  <div class="thumb thumb--office" style="left:45px;top:514px" role="img" aria-label="Office workstations under LED lighting"></div>
  <div class="thumb thumb--warehouse" style="left:206px;top:514px" role="img" aria-label="Warehouse with hi-bay lighting"></div>
  <div class="thumb thumb--home" style="left:379px;top:514px" role="img" aria-label="Modern home interior with downlights"></div>
  <footer class="footer">
    <ul class="contact">
      <li><svg viewBox="0 0 10 10"><circle cx="5" cy="5" r="4" fill="none" stroke="#fff" stroke-width="1.2"/><circle cx="5" cy="5" r="1.6" fill="#fff"/></svg>rtwexmoorelectrical@quillmail.test</li>
      <li><svg viewBox="0 0 10 10"><circle cx="5" cy="5" r="4" fill="none" stroke="#fff" stroke-width="1.2"/><path d="M5 2.5a1.6 1.6 0 0 1 1.6 1.6C6.6 5.3 5 7.5 5 7.5S3.4 5.3 3.4 4.1A1.6 1.6 0 0 1 5 2.5z" fill="#fff"/></svg>PO Box 58 Brambleton Vale VIC 3179</li>
    </ul>
    <div class="quote">
      <svg class="quote__icon" viewBox="0 0 26 58"><path d="M18 2h6v16h-6c-3 0-4 3-4 11s1 11 4 11h6v16h-6C7 56 2 44 2 29S7 2 18 2z" fill="#fff"/></svg>
      <div>
        <div class="quote__label">CALL DEREK FOR A QUOTE</div>
        <div class="quote__number">0418 736 204</div>
      </div>
    </div>
  </footer>
</section>

<!-- BACK -->
<section class="flyer flyer--back">
  <div class="back__photo" role="img" aria-label="Rooftop array of solar PV panels under a blue sky"></div>
  <svg class="back__header" viewBox="0 0 540 120" aria-hidden="true">
    <polygon points="0,0 366,0 306,112 0,112" fill="var(--green)"/>
    <polygon points="0,0 356,0 300,104 0,104" fill="#f4f4f4"/>
  </svg>
  <div class="brand back__brand">
    <span class="brand__dot"></span>
    <div class="brand__name">R.T. Wexmoor<br>Electrical</div>
  </div>
  <div class="band band--dark back__band">RESIDENTIAL, COMMERCIAL, &amp; INDUSTRIAL ELECTRICAL WORKS</div>
  <div class="band band--green back__band2">INCLUDING PV SOLAR SYSTEM DESIGNS &amp; INSTALLATIONS</div>
  <ul class="services services--left">
    <li>Maintenance</li><li>System Checks &amp; Upgrades</li><li>Mains Upgrades</li><li>Overhead &amp; Underground</li>
    <li>Switchboard Installations &amp; Upgrades</li><li>Safety Switches</li><li>Spa &amp; Pool connections</li><li>LED Lighting solutions</li>
  </ul>
  <ul class="services services--right">
    <li>Energy Audit Checks</li><li>Fans &amp; Air Conditioning</li><li>Hi-bay Lighting</li><li>Carpark Lighting</li>
    <li>Data Points</li><li>Comms Racks</li><li>New Home Builds</li><li>Office Fitouts ...</li>
  </ul>
  <div class="thumb thumb--spa" style="left:37px;top:480px" role="img" aria-label="Illuminated spa with blue underwater lights"></div>
  <div class="thumb thumb--board" style="left:199px;top:480px" role="img" aria-label="Open switchboard with circuit breakers"></div>
  <div class="thumb thumb--carpark" style="left:372px;top:480px" role="img" aria-label="Carpark lit by pole lights at night"></div>
  <div class="partners" aria-label="Partner brands">
    <span style="width:50px"></span><span style="width:44px"></span><span style="width:22px"></span><span style="width:32px"></span>
    <span style="width:60px"></span><span style="width:70px"></span><span style="width:44px"></span><span style="width:70px"></span>
    <span style="width:40px"></span><span style="width:56px"></span>
  </div>
  <footer class="footer">
    <ul class="contact">
      <li><svg viewBox="0 0 10 10"><circle cx="5" cy="5" r="4" fill="none" stroke="#fff" stroke-width="1.2"/><circle cx="5" cy="5" r="1.6" fill="#fff"/></svg>rtwexmoorelectrical@quillmail.test</li>
      <li><svg viewBox="0 0 10 10"><circle cx="5" cy="5" r="4" fill="none" stroke="#fff" stroke-width="1.2"/><path d="M5 2.5a1.6 1.6 0 0 1 1.6 1.6C6.6 5.3 5 7.5 5 7.5S3.4 5.3 3.4 4.1A1.6 1.6 0 0 1 5 2.5z" fill="#fff"/></svg>PO Box 58 Brambleton Vale VIC 3179</li>
    </ul>
    <div class="quote">
      <svg class="quote__icon" viewBox="0 0 26 58"><path d="M18 2h6v16h-6c-3 0-4 3-4 11s1 11 4 11h6v16h-6C7 56 2 44 2 29S7 2 18 2z" fill="#fff"/></svg>
      <div>
        <div class="quote__label">CALL DEREK FOR A QUOTE</div>
        <div class="quote__number">0418 736 204</div>
      </div>
    </div>
  </footer>
</section>

</body>
</html>
```